Bright Tooth Dentistry Business Card

We need business cards for our dental office.
We are looking for a clean, elegant design

We provide dental services to children.
Our card needs to be appealing to referring dentists, parents and our team

Target Market(s)

referring dentists, parents and our team

Industry/Entity Type

Dental Clinic

Contact Information for Business Card

4816 Juniper Lane, Suite 100
Oakmont Heights, PA 15237

412-837-2961 Voice
412-837-2962 fax
info@brighttoothdentalpa.com email
www.brighttoothdentalpa.com web

Font styles to use
Sans Serif

Requirements
Must have
• White background - clean, crisp, elegant, simple
• rounded corners
• different color palate - once we come up with design, we will replace the blue with orange, green,
Nice to have
• Follow our logo typeface and colors
• then we can replace color

```html
<!DOCTYPE html>
<html lang="en">
<head>
<meta charset="UTF-8">
<title>Bright Tooth Dentistry Business Card</title>
<link rel="stylesheet" href="https://fonts.googleapis.com/css2?family=Quicksand:wght@500;600;700&display=swap">
<style>
  :root {
    --backdrop: #cfcfcf;
    --card-white: #ffffff;
    --brand-orange: #f7991c;
    --text-grey: #7a7a7a;
    --divider-grey: #b9b9b9;
  }
  * { margin: 0; padding: 0; box-sizing: border-box; }
  html, body {
    width: 900px;
    height: 1200px;
    overflow: hidden;
    background: var(--backdrop);
    font-family: "Quicksand", sans-serif;
  }
  .canvas { position: relative; width: 900px; height: 1200px; }
  .card {
    position: absolute;
    left: 80px;
    width: 735px;
    height: 430px;
    border-radius: 22px;
    overflow: hidden;
  }
  .card-front { top: 127px; background: var(--card-white); }
  .card-front .edge-band {
    position: absolute; left: 0; right: 0; bottom: 0; height: 10px;
    background: var(--brand-orange);
  }
  .card-back { top: 645px; background: var(--brand-orange); }

  .brand {
    position: absolute; left: 0; right: 0;
    display: flex; flex-direction: column; align-items: center;
  }
  .card-front .brand { top: 100px; }
  .card-back .brand { top: 140px; }
  .brand-dot {
    width: 46px; height: 46px; border-radius: 50%;
    background: var(--brand-orange);
    margin-bottom: 22px;
  }
  .card-back .brand-dot { background: var(--card-white); }
  .brand-name {
    font-weight: 700; font-size: 36px; line-height: 1; letter-spacing: -0.3px;
    color: var(--brand-orange);
  }
  .card-back .brand-name { color: var(--card-white); }

  .address {
    position: absolute; right: 385px; top: 294px;
    text-align: right; font-style: normal; font-weight: 600; font-size: 17px; line-height: 26px;
    color: var(--text-grey);
  }
  .divider {
    position: absolute; left: 366px; top: 272px; width: 1px; height: 96px;
    background: var(--divider-grey);
  }
  .contacts {
    position: absolute; left: 388px; top: 268px; list-style: none;
    font-weight: 600; font-size: 17px; line-height: 26px; color: var(--text-grey);
  }
  .contacts li { display: flex; align-items: center; gap: 12px; }
  .contacts svg { width: 18px; height: 18px; fill: var(--brand-orange); flex: none; }
</style>
</head>
<body>
<main class="canvas">
  <section class="card card-front" aria-label="Card front">
    <div class="brand">
      <span class="brand-dot"></span>
      <span class="brand-name">Bright Tooth Dentistry</span>
    </div>
    <address class="address">
      4816 Juniper Lane, Suite 210<br>
      Oakmont Heights, PA 15237
    </address>
    <span class="divider"></span>
    <ul class="contacts">
      <li>
        <svg viewBox="0 0 24 24" aria-hidden="true"><path d="M6.6 10.8c1.4 2.8 3.8 5.1 6.6 6.6l2.2-2.2c.3-.3.7-.4 1-.2 1.1.4 2.3.6 3.6.6.6 0 1 .4 1 1V20c0 .6-.4 1-1 1C10.6 21 3 13.4 3 4c0-.6.4-1 1-1h3.5c.6 0 1 .4 1 1 0 1.3.2 2.5.6 3.6.1.3 0 .7-.2 1l-2.3 2.2z"/></svg>
        <span>412-837-2961</span>
      </li>
      <li>
        <svg viewBox="0 0 24 24" aria-hidden="true"><path d="M6 3h12v5H6zM3 9h18v8h-3v-3H6v3H3zM7 15h10v6H7z"/></svg>
        <span>412-837-2962</span>
      </li>
      <li>
        <svg viewBox="0 0 24 24" aria-hidden="true"><path d="M2 5h20v14H2zM4 7v.5l8 5.5 8-5.5V7l-8 5.5z"/></svg>
        <span>info@brighttoothdentalpa.com</span>
      </li>
      <li>
        <svg viewBox="0 0 24 24" aria-hidden="true"><path d="M12 2a10 10 0 1 0 0 20 10 10 0 0 0 0-20zm6.9 6h-2.9a15 15 0 0 0-1.4-3.6A8 8 0 0 1 18.9 8zM12 4c.8 1.2 1.5 2.5 1.9 4h-3.8c.4-1.5 1.1-2.8 1.9-4zM4.3 14a8 8 0 0 1 0-4h3.4a16 16 0 0 0 0 4zm.8 2h2.9c.3 1.3.8 2.5 1.4 3.6A8 8 0 0 1 5.1 16zM8 8H5.1a8 8 0 0 1 4.3-3.6C8.8 5.5 8.4 6.7 8 8zm4 12c-.8-1.2-1.5-2.5-1.9-4h3.8c-.4 1.5-1.1 2.8-1.9 4zm2.3-6H9.7a14 14 0 0 1 0-4h4.6a14 14 0 0 1 0 4zm.3 5.6c.6-1.1 1.1-2.3 1.4-3.6h2.9a8 8 0 0 1-4.3 3.6zm1.7-5.6a16 16 0 0 0 0-4h3.4a8 8 0 0 1 0 4z"/></svg>
        <span>www.brighttoothdentalpa.com</span>
      </li>
    </ul>
    <span class="edge-band"></span>
  </section>

  <section class="card card-back" aria-label="Card back">
    <div class="brand">
      <span class="brand-dot"></span>
      <span class="brand-name">Bright Tooth Dentistry</span>
    </div>
  </section>
</main>
</body>
</html>
```